i need a template design for online store

hi great designers, i need a template for any online store. But preferably well owned shopping carts. I would be an added advantage if the store is setup for me. I need a mature and attractive colours. My online store deals in electronics.

Shopping

1 page

```html
<!DOCTYPE html>
<html lang="en">
<head>
<meta charset="utf-8">
<title>Vendora – Online Store</title>
<link rel="stylesheet" href="https://fonts.googleapis.com/css2?family=Open+Sans:wght@400;600;700&family=Raleway:wght@400;500&display=swap">
<style>
:root{
  --brown:#5b3c29;
  --red:#dd5450;
  --cyan:#1fb8e6;
  --green:#8aae6c;
  --beige:#f3e7d5;
  --cream:#f6ebdc;
  --page:#f5f4f2;
  --ink:#3a2c24;
  --muted:#7a6e66;
  --price:#3aa6d8;
  --line:#e4ddd3;
}
*{margin:0;padding:0;box-sizing:border-box}
html,body{width:783px;height:1200px;overflow:hidden}
body{position:relative;background:var(--page);font-family:"Open Sans",Arial,sans-serif;color:var(--ink);font-size:6px}
.abs{position:absolute}
.topbar{left:0;top:0;width:783px;height:20px;background:var(--brown);color:#fff;font-size:5.5px}
.topbar span{position:absolute;top:7px}
.header{left:0;top:20px;width:783px;height:70px;background:#fff}
.logo{left:150px;top:34px;font-size:15px;font-weight:600;color:var(--brown);display:flex;align-items:center;gap:5px}
.logo i{width:8px;height:8px;background:var(--red);display:block}
.delivery{left:275px;top:34px;font-size:5.5px;color:var(--muted);display:flex;align-items:center;gap:4px}
.search{left:388px;top:30px;width:145px;height:17px;border:1px solid var(--red);background:#fff;font-size:5px;color:#999;padding:5px 6px}
.search-btn{left:533px;top:30px;width:28px;height:17px;background:var(--red)}
.cart{left:576px;top:30px;width:57px;height:17px;background:var(--red);color:#fff;font-size:5px}
.cart b{position:absolute;left:-1px;top:-5px;width:8px;height:8px;background:var(--red);border:1px solid #fff;border-radius:50%;font-size:4px;text-align:center;line-height:6px}
.nav{left:152px;top:77px;display:flex;gap:6px;font-size:5.5px;color:var(--ink)}
.nav span{padding:2px 3px}
.nav .on{background:var(--red);color:#fff}
.navline{left:0;top:89px;width:783px;height:2px;background:var(--red)}
.hero{left:151px;top:95px;width:482px;height:130px;background:linear-gradient(90deg,#f7ecde,#f3e3cf)}
.hero h2{position:absolute;left:41px;top:18px;font-family:Raleway,sans-serif;font-weight:500;font-size:10px;color:var(--ink)}
.hero .pct{position:absolute;left:41px;top:38px;font-size:16px;color:var(--ink)}
.hero .pct small{font-size:5px}
.hero p{position:absolute;left:41px;top:64px;width:170px;font-size:4.5px;line-height:7px;color:var(--muted)}
.hero .more{position:absolute;left:41px;top:87px;width:32px;height:11px;background:var(--red);color:#fff;font-size:4.5px;text-align:center;line-height:11px}
.hero .circle{position:absolute;left:280px;top:5px;width:130px;height:130px;border-radius:50%;background:#f2dfc6}
.hero .sale{position:absolute;left:298px;top:28px;font-family:Raleway,sans-serif;font-size:16px;color:var(--ink)}
.hero .off{position:absolute;left:298px;top:50px;font-size:12px;color:var(--red);font-weight:700}
.hero .off small{font-size:4px;font-weight:400}
.hero .view{position:absolute;left:300px;top:76px;width:46px;height:10px;background:var(--brown);color:#fff;font-size:4px;text-align:center;line-height:10px}
.hero .bag{position:absolute;left:363px;top:20px;width:75px;height:88px;border-radius:8px;background:linear-gradient(160deg,#e9d9c8,#c9a78a)}
.hero .arr{position:absolute;right:6px;top:58px;color:#ddd;font-size:12px}
.feat{top:233px;width:111px;height:41px;color:#fff;font-size:5.5px;line-height:8px;padding:11px 0 0 28px}
.feat svg{position:absolute;left:6px;top:9px}
.tagline{left:0;top:290px;width:783px;text-align:center;font-family:Raleway,sans-serif;font-size:17.5px;color:var(--ink)}
.tagsub{left:0;top:312px;width:783px;text-align:center;font-size:6px;color:var(--muted)}
.dash{left:151px;top:328px;width:482px;border-top:1px dashed #cfc6bb}
.bar{height:19px;background:var(--beige);font-size:9.5px;color:var(--ink);padding:3px 0 0 23px}
.bar svg{position:absolute;left:6px;top:5px}
.card{top:370px;width:111px;height:140px;background:#fff}
.card .ph{height:90px}
.card .corner{position:absolute;right:0;top:0;width:0;height:0;border-top:14px solid var(--cyan);border-left:14px solid transparent}
.card .name{position:absolute;top:96px;width:100%;text-align:center;font-size:6px}
.card .pr{position:absolute;top:108px;width:100%;text-align:center;font-size:6.5px;color:var(--price)}
.card .btns{position:absolute;top:123px;left:0;width:100%;height:16px;display:flex;justify-content:space-between}
.card .add{width:48px;background:var(--green);color:#fff;font-size:4.5px;line-height:16px;text-align:center}
.card .see{width:48px;background:var(--red);color:#fff;font-size:4.5px;line-height:16px;text-align:center}
.card .heart{position:absolute;left:0;top:84px;width:10px;height:10px;background:var(--red);border-radius:50%}
.promo-band{left:0;top:530px;width:783px;height:220px;background:#fff}
.promo-title{left:0;top:550px;width:783px;text-align:center;font-size:10.5px;color:var(--ink)}
.pcard{top:582px;width:70px;height:129px;background:var(--cream)}
.pcard .ph{height:81px}
.pcard .corner{position:absolute;right:0;top:0;border-top:12px solid var(--cyan);border-left:12px solid transparent}
.pcard .name{position:absolute;top:87px;width:100%;text-align:center;font-size:6px}
.pcard .pr{position:absolute;top:99px;width:100%;text-align:center;font-size:6px;color:var(--price)}
.pcard .add{position:absolute;left:0;top:113px;width:100%;height:16px;background:var(--green);color:#fff;font-size:6px;line-height:16px;padding-left:25px}
.chev{top:622px;font-size:16px;color:var(--ink);font-weight:700}
.dots{left:376px;top:731px;display:flex;gap:2px}
.dots i{width:5px;height:5px;border-radius:50%;border:1px solid #888;display:block}
.dots i.on{background:#555}
.sep{left:0;top:749px;width:783px;height:3px;background:var(--line)}
.deal{left:151px;top:801px;width:154px;height:170px;border:2px solid var(--green);background:#fff}
.deal .ph{position:absolute;left:0;top:0;width:150px;height:106px}
.count{position:absolute;left:0;top:44px;display:flex}
.count div{width:27px;height:20px;background:rgba(255,255,255,.8);text-align:center;font-size:11px;color:var(--green);line-height:12px;margin-right:2px}
.count small{display:block;font-size:3.5px;line-height:5px;color:var(--muted)}
.deal .name{position:absolute;top:114px;width:100%;text-align:center;font-size:8.5px}
.deal .old{position:absolute;left:38px;top:129px;font-size:5.5px}
.deal .new{position:absolute;left:76px;top:126px;font-size:9px;color:var(--red)}
.deal .buy{position:absolute;left:0;bottom:0;width:100%;height:24px;background:var(--green);color:#fff;font-size:12px;line-height:24px;padding-left:45px}
.post{left:315px;width:318px;height:40px;border-bottom:1px dashed #cfc6bb}
.post .th{position:absolute;left:0;top:0;width:30px;height:28px}
.post h4{position:absolute;left:41px;top:1px;font-weight:400;font-size:7px}
.post p{position:absolute;left:41px;top:10px;width:250px;font-size:4.3px;line-height:5.5px;color:var(--muted)}
.post .go{position:absolute;right:0;top:17px;width:22px;height:10px;background:var(--green)}
.foot-band{left:0;top:995px;width:783px;height:155px;background:#fff}
.fh{top:1011px;width:111px;height:18px;background:var(--beige);font-size:10px;padding:2px 0 0 24px}
.fh svg{position:absolute;left:6px;top:5px}
.ftext{font-size:4.3px;line-height:5.8px;color:var(--muted)}
.social{top:1042px;width:14px;height:14px;background:#2f6fa8}
.bottom{left:0;top:1150px;width:783px;height:50px;background:var(--brown)}
.pay{top:10px;width:16px;height:10px;background:#9a8a7d}
.flinks{left:0;top:31px;width:783px;text-align:center;font-size:4.5px;color:#d9c9bb;word-spacing:14px}
.copy{left:0;top:41px;width:783px;text-align:center;font-size:3.8px;color:#bfae9f}
</style>
</head>
<body>

<div class="abs topbar">
  <span style="left:155px">$ AUD ▾</span>
  <span style="left:188px;display:flex;gap:3px;align-items:center"><i style="width:7px;height:5px;background:#fff;display:block"></i>Langue</span>
  <span style="left:537px">Bienvenu</span>
  <span style="left:565px">S'inscrire</span>
  <span style="left:592px">Login</span>
  <span style="left:610px">Aide</span>
</div>

<div class="abs header"></div>
<div class="abs logo"><i></i>Vendora</div>
<div class="abs delivery">
  <svg width="9" height="9" viewBox="0 0 10 10"><circle cx="5" cy="5" r="4" fill="none" stroke="#777" stroke-width="1"/><path d="M5 2.5V5l2 1" stroke="#777" fill="none"/></svg>
  Livraison 24h/48
</div>
<div class="abs search">Mot clé ou référence...</div>
<div class="abs search-btn"><svg width="28" height="17" viewBox="0 0 28 17"><circle cx="13" cy="8" r="3.5" fill="none" stroke="#fff" stroke-width="1.3"/><path d="M15.5 10.5l3 3" stroke="#fff" stroke-width="1.3"/></svg></div>
<div class="abs cart">
  <b>2</b>
  <svg class="abs" style="left:10px;top:4px" width="8" height="9" viewBox="0 0 8 9"><rect x="1" y="3" width="6" height="5.5" fill="none" stroke="#fff"/><path d="M2.5 3V1.5h3V3" fill="none" stroke="#fff"/></svg>
  <span class="abs" style="left:32px;top:5px">200,00 $</span>
</div>
<div class="abs nav">
  <span class="on">HOME</span><span>SPECIAL</span><span>MEN FASHION</span><span>ACCESSORIES</span><span>WOMEN'S FASHION</span><span>BLOG</span>
</div>
<div class="abs navline"></div>

<section class="abs hero">
  <h2>2014 NEW ARRIVALS GET UP TO</h2>
  <div class="pct">25% <small>OFF</small></div>
  <p>Proin gravida nibh vel velit auctor aliquet nibh vel velit auctor aliquet. Aenean sollicitudin.</p>
  <div class="more">More</div>
  <div class="circle"></div>
  <div class="sale">BIG SALE</div>
  <div class="off">10 <small>%OFF<br>for first order every day</small></div>
  <div class="view">VIEW COLLECTION</div>
  <div class="bag" role="img" aria-label="Leather handbag product photo"></div>
  <div class="arr">›</div>
</section>

<div class="abs feat" style="left:151px;background:var(--cyan)">
  <svg width="18" height="22" viewBox="0 0 18 22"><rect x="2" y="7" width="14" height="14" fill="none" stroke="#fff" stroke-width="1.8"/><path d="M5 7V4a4 4 0 0 1 8 0v3" fill="none" stroke="#fff" stroke-width="1.8"/></svg>
  Upto 5% Reward<br>on your shipping</div>
<div class="abs feat" style="left:273px;width:112px;background:linear-gradient(90deg,#dcae94,#e9c9b6)">
  <svg width="20" height="20" viewBox="0 0 20 20"><circle cx="10" cy="10" r="8.5" fill="none" stroke="#fff" stroke-width="1.6"/><path d="M10 4v6l4 2" fill="none" stroke="#fff" stroke-width="1.6"/></svg>
  Easy Extended<br>Returned</div>
<div class="abs feat" style="left:398px;background:var(--red)">
  <svg width="22" height="18" viewBox="0 0 22 18"><rect x="1" y="4" width="12" height="9" fill="#fff"/><path d="M13 7h4l3 3v3h-7z" fill="#fff"/><circle cx="5" cy="15" r="2" fill="#fff"/><circle cx="16" cy="15" r="2" fill="#fff"/></svg>
  Free Shipping on<br>order over 99 $</div>
<div class="abs feat" style="left:521px;width:112px;background:#7b7b7b">
  <svg width="16" height="22" viewBox="0 0 16 22"><text x="3" y="18" fill="#fff" font-size="20" font-family="Arial">$</text></svg>
  Delivery Schedule<br>Spread Cheer Time</div>

<h1 class="abs tagline" style="font-weight:400">1 OF THE MOST BEAUTIFUL ONLINE STORE</h1>
<div class="abs tagsub">Clothes is one of the world's leading E-commerce companies that designs and develops online stores</div>
<div class="abs dash"></div>

<div class="abs bar" style="left:151px;top:340px;width:482px">
  <svg width="9" height="9" viewBox="0 0 10 10"><path d="M5 0l1.5 3.3 3.5.4-2.6 2.4.7 3.5L5 7.8 1.9 9.6l.7-3.5L0 3.7l3.5-.4z" fill="var(--ink)"/></svg>Best Sellers</div>

<div class="abs card" style="left:151px"><div class="ph" role="img" aria-label="Red leather jacket product photo" style="background:linear-gradient(160deg,#f1f1f1,#d63b3f 60%,#e9e9e9)"></div><div class="corner"></div><div class="heart"></div><div class="name">Red leather jaquette</div><div class="pr">189,90 $</div><div class="btns"><div class="add">Add to Cart</div><div class="see">See More</div></div></div>
<div class="abs card" style="left:274px"><div class="ph" role="img" aria-label="Brown leather wristwatch product photo" style="background:linear-gradient(160deg,#f3f3f3,#5e3b2a 55%,#eee)"></div><div class="corner"></div><div class="heart"></div><div class="name">Yellowbrown jaquette</div><div class="pr">19,00 $</div><div class="btns"><div class="add">Add to Cart</div><div class="see">See More</div></div></div>
<div class="abs card" style="left:398px"><div class="ph" role="img" aria-label="Man in sports jacket, city background product photo" style="background:linear-gradient(180deg,#9fb3c6,#6f7b88 60%,#3c3d40)"></div><div class="corner"></div><div class="heart"></div><div class="name">White robe un truc</div><div class="pr">589,90 $</div><div class="btns"><div class="add">Add to Cart</div><div class="see">See More</div></div></div>
<div class="abs card" style="left:521px"><div class="ph" role="img" aria-label="Couple in winter jackets product photo" style="background:linear-gradient(180deg,#8a8d95,#8b6a4c 55%,#3b4556)"></div><div class="corner"></div><div class="heart"></div><div class="name">Un autre truc pour</div><div class="pr">19,95 $</div><div class="btns"><div class="add">Add to Cart</div><div class="see">See More</div></div></div>

<div class="abs promo-band"></div>
<div class="abs promo-title">
  <svg width="9" height="9" viewBox="0 0 10 10" style="margin-right:6px;vertical-align:-1px"><path d="M0 5V0h5l5 5-5 5z" fill="var(--ink)"/><circle cx="2.5" cy="2.5" r="1" fill="#fff"/></svg>Promotion</div>
<div class="abs chev" style="left:160px">‹</div>
<div class="abs chev" style="left:613px">›</div>

<div class="abs pcard" style="left:191px"><div class="ph" role="img" aria-label="Man in purple sleeveless shirt photo" style="background:linear-gradient(180deg,#a9c7de,#6a5b8f 60%,#c9c4d6)"></div><div class="corner"></div><div class="name">White robe un truc</div><div class="pr">589,90 $</div><div class="add">Add to Cart</div></div>
<div class="abs pcard" style="left:273px"><div class="ph" role="img" aria-label="Man in hat and brown coat photo" style="background:linear-gradient(180deg,#d8d3cc,#6a4b35 55%,#3c2d24)"></div><div class="corner"></div><div class="name">White robe un truc</div><div class="pr">589,90 $</div><div class="add">Add to Cart</div></div>
<div class="abs pcard" style="left:355px"><div class="ph" role="img" aria-label="Diamond ring product photo" style="background:radial-gradient(circle,#c9b08a,#cfcfcf 45%,#f5f5f5)"></div><div class="corner"></div><div class="name">Princes Diamonds</div><div class="pr">589,90 $</div><div class="add">Add to Cart</div></div>
<div class="abs pcard" style="left:438px"><div class="ph" role="img" aria-label="Man in navy blazer photo" style="background:linear-gradient(180deg,#f2f2f2,#2d3b55 45%,#d9cbb4)"></div><div class="corner"></div><div class="name">White robe un truc</div><div class="pr">589,90 $</div><div class="add">Add to Cart</div></div>
<div class="abs pcard" style="left:521px"><div class="ph" role="img" aria-label="Man in dark suit, new for men photo" style="background:linear-gradient(180deg,#8c8f93,#2c2e33 60%,#555)"></div><div class="corner"></div><div class="name">White robe un truc</div><div class="pr">589,90 $</div><div class="add">Add to Cart</div></div>

<div class="abs dots"><i></i><i></i><i></i><i></i><i class="on"></i></div>
<div class="abs sep"></div>

<div class="abs bar" style="left:151px;top:768px;width:154px">
  <svg width="9" height="9" viewBox="0 0 10 10"><path d="M5 0v3M5 7v3M0 5h3M7 5h3M1.5 1.5l2 2M6.5 6.5l2 2M8.5 1.5l-2 2M3.5 6.5l-2 2" stroke="var(--ink)"/></svg>Tous nos produits</div>
<div class="abs deal">
  <div class="ph" role="img" aria-label="Patterned dress with sunglasses, handbag and sandals photo" style="background:linear-gradient(135deg,#f4f4f4,#2e3f73 50%,#e8d6c2)"></div>
  <div class="count">
    <div>46<small>Days</small></div><div>19<small>Hours</small></div><div>65<small>Minutes</small></div><div>20<small>Seconds</small></div>
  </div>
  <div class="name">Petites Mink Twill Jacket</div>
  <div class="old">$120.00</div>
  <div class="new">$100.00</div>
  <div class="buy">
    <svg class="abs" style="left:8px;top:6px" width="14" height="12" viewBox="0 0 14 12"><path d="M1 4h12l-2 7H3z" fill="#fff"/><path d="M4 4l3-3 3 3" stroke="#fff" fill="none"/></svg>Buy this deal</div>
</div>

<div class="abs bar" style="left:315px;top:768px;width:318px">
  <svg width="9" height="9" viewBox="0 0 10 10"><rect x="0" y="0" width="10" height="10" fill="var(--ink)"/><path d="M2 3h6M2 5h6M2 7h4" stroke="#fff"/></svg>From the blog</div>

<article class="abs post" style="top:800px"><div class="th" role="img" aria-label="Blog thumbnail, woman portrait" style="background:linear-gradient(135deg,#d9b7c0,#8d5a6a)"></div><h4>here are many variations of passages of Lorem Ipsum available,</h4><p>but the majority have suffered alteration in some form, by injected humour, or randomised words which don't look even slightly believable. If you are going to use a passage of Lorem Ipsum, you need to be sure there isn't anything embarrassing hidden in the middle of text.</p><div class="go"><svg width="22" height="10" viewBox="0 0 22 10"><path d="M6 5h9M12 2l3 3-3 3" stroke="#fff" fill="none"/></svg></div></article>
<article class="abs post" style="top:847px"><div class="th" role="img" aria-label="Blog thumbnail, small airplane in sky" style="background:linear-gradient(180deg,#8fc3ea,#d8e9f5)"></div><h4>here are many variations of passages of Lorem Ipsum available,</h4><p>but the majority have suffered alteration in some form, by injected humour, or randomised words which don't look even slightly believable. If you are going to use a passage of Lorem Ipsum, you need to be sure there isn't anything embarrassing hidden in the middle of text.</p><div class="go"><svg width="22" height="10" viewBox="0 0 22 10"><path d="M6 5h9M12 2l3 3-3 3" stroke="#fff" fill="none"/></svg></div></article>
<article class="abs post" style="top:893px"><div class="th" role="img" aria-label="Blog thumbnail, red tulips" style="background:linear-gradient(180deg,#d3333b,#4f7a3a)"></div><h4>here are many variations of passages of Lorem Ipsum available,</h4><p>but the majority have suffered alteration in some form, by injected humour, or randomised words which don't look even slightly believable. If you are going to use a passage of Lorem Ipsum, you need to be sure there isn't anything embarrassing hidden in the middle of text.</p><div class="go"><svg width="22" height="10" viewBox="0 0 22 10"><path d="M6 5h9M12 2l3 3-3 3" stroke="#fff" fill="none"/></svg></div></article>
<article class="abs post" style="top:940px"><div class="th" role="img" aria-label="Blog thumbnail, silver car" style="background:linear-gradient(180deg,#eee,#9ea3a8)"></div><h4>here are many variations of passages of Lorem Ipsum available,</h4><p>but the majority have suffered alteration in some form, by injected humour, or randomised words which don't look even slightly believable. If you are going to use a passage of Lorem Ipsum, you need to be sure there isn't anything embarrassing hidden in the middle of text.</p><div class="go"><svg width="22" height="10" viewBox="0 0 22 10"><path d="M6 5h9M12 2l3 3-3 3" stroke="#fff" fill="none"/></svg></div></article>

<div class="abs foot-band"></div>
<div class="abs fh" style="left:151px"><svg width="9" height="9" viewBox="0 0 10 10"><path d="M5 0l4.5 2.5v5L5 10 .5 7.5v-5z" fill="var(--ink)"/></svg>Nos boutiques</div>
<div class="abs fh" style="left:273px;width:112px"><svg width="9" height="9" viewBox="0 0 10 10"><path d="M0 0h10v7H4l-3 3V7H0z" fill="var(--ink)"/></svg>About</div>
<div class="abs fh" style="left:398px"><svg width="9" height="9" viewBox="0 0 10 10"><path d="M5 0l4.5 2.5v5L5 10 .5 7.5v-5z" fill="var(--ink)"/></svg>Contact us</div>
<div class="abs fh" style="left:521px;width:112px"><svg width="9" height="9" viewBox="0 0 10 10"><path d="M5 0l4.5 2.5v5L5 10 .5 7.5v-5z" fill="var(--ink)"/></svg>Contact us</div>

<div class="abs" role="img" aria-label="Store interior with display counters" style="left:151px;top:1040px;width:111px;height:82px;background:linear-gradient(180deg,#3a5a8c,#c9d3e2 55%,#7a8796)"></div>
<div class="abs ftext" style="left:273px;top:1040px;width:112px">but the majority have suffered alteration in some form, by injected humour, or randomised words which don't look even slightly believable. If you are going to use a passage of Lorem Ipsum, you need to be sure there isn't anything embarrassing hidden in the middle of text.<br><br>but the majority have suffered alteration in some form, by injected humour, or randomised words which don't look even slightly believable. If you are going to use a passage of Lorem Ipsum, you need to be sure there isn't anything embarrassing hidden in the middle of text.</div>

<div class="abs social" style="left:398px"></div>
<div class="abs social" style="left:422px;background:#2b8fc8"></div>
<div class="abs social" style="left:446px;background:#b6b6b6"></div>
<div class="abs social" style="left:471px;background:#2a6fa3"></div>
<div class="abs social" style="left:495px;background:#3aa0d8"></div>

<div class="abs ftext" style="left:521px;top:1040px;width:112px">12 Market Lane, Harbor City<br>+00 123 456 789<br>vendora.shop<br>hello@vendora.shop<br>orders@vendora.shop</div>

<footer class="abs bottom">
  <div class="abs pay" style="left:333px"></div>
  <div class="abs pay" style="left:352px"></div>
  <div class="abs pay" style="left:372px"></div>
  <div class="abs pay" style="left:392px"></div>
  <div class="abs pay" style="left:413px;background:#b9aca0"></div>
  <div class="abs pay" style="left:433px;background:#b9aca0"></div>
  <div class="flinks abs">Home Blog Shop Media Features About Us Contact Us</div>
  <div class="copy abs">Copyright © 2014 Vendora.</div>
</footer>

</body>
</html>
```